Wholesale in Gold Jewellery & Gold Bullion

We are an established gold jewellery and gold bullion wholesaler selling these products to international clients. We already have a name and logo of our company, hence please view attached current card design. We need a completely new design to compliment our business and industry and the final design should be new and elegant.

Contact Information for Business Card

New card details must be same as per current card. Like logo, name, tel no. & etc.

Colors

Designer to choose colors to be used in the design.

```html
<!DOCTYPE html>
<html lang="en">
<head>
<meta charset="utf-8">
<title>Arven &amp; Co – Business Card</title>
<link href="https://fonts.googleapis.com/css2?family=Libre+Baskerville:wght@700&family=Lato:wght@400&family=Montserrat:wght@300;400&display=swap" rel="stylesheet">
<style>
  :root {
    --gold: #d29a2c;
    --card: #ffffff;
    --backdrop: #2a2827;
  }
  * { box-sizing: border-box; margin: 0; padding: 0; }
  html, body { width: 1200px; height: 800px; overflow: hidden; background: var(--backdrop); }
  .canvas { position: relative; width: 1200px; height: 800px; }
  .card {
    position: absolute; left: 75px; top: 100px;
    width: 1050px; height: 600px;
    background: var(--card); color: var(--gold);
    overflow: hidden;
  }
  .company {
    position: absolute; left: 52px; top: 52px;
    font-family: "Libre Baskerville", "Times New Roman", serif;
    font-weight: 700; font-size: 44px; letter-spacing: 1px;
  }
  .address {
    position: absolute; left: 54px; top: 112px;
    font-family: "Lato", Arial, sans-serif; font-size: 28px;
  }
  .accent-bar {
    position: absolute; left: 0; top: 228px;
    width: 14px; height: 86px; background: var(--gold);
  }
  .person { position: absolute; left: 54px; top: 222px; font-family: "Lato", Arial, sans-serif; }
  .person-name { font-size: 38px; line-height: 1.15; }
  .person-title { font-size: 27px; margin-left: 8px; }
  .rules { position: absolute; left: 0; top: 0; }
  .brand-mark {
    position: absolute; left: 720px; top: 200px; width: 170px;
    text-align: center;
  }
  .brand-dot {
    width: 130px; height: 130px; border-radius: 50%;
    background: var(--gold); margin: 0 auto 14px;
  }
  .brand-name {
    font-family: "Libre Baskerville", "Times New Roman", serif;
    font-weight: 700; font-size: 28px; letter-spacing: 2px;
  }
  .contacts {
    position: absolute; left: 58px; top: 432px; list-style: none;
    font-family: "Montserrat", Arial, sans-serif; font-weight: 300; font-size: 25px;
  }
  .contacts li { display: flex; align-items: center; height: 36px; }
  .contacts svg { width: 22px; height: 22px; margin-right: 14px; fill: var(--gold); }
</style>
</head>
<body>
<div class="canvas">
  <div class="card">
    <div class="company">ARVEN &amp; CO PTE LTD</div>
    <div class="address">52 Linden Row, Singapore 408215</div>

    <div class="accent-bar"></div>
    <div class="person">
      <div class="person-name">Rohan Veltani</div>
      <div class="person-title">Director</div>
    </div>

    <svg class="rules" width="1050" height="600" aria-hidden="true">
      <g stroke="#d29a2c" stroke-width="4">
        <line x1="52" y1="392" x2="720" y2="392"/>
        <line x1="52" y1="410" x2="720" y2="410"/>
        <line x1="890" y1="256" x2="1000" y2="256"/>
        <line x1="890" y1="274" x2="1000" y2="274"/>
      </g>
    </svg>

    <div class="brand-mark">
      <div class="brand-dot"></div>
      <div class="brand-name">ARVEN</div>
    </div>

    <ul class="contacts">
      <li><svg viewBox="0 0 24 24"><path d="M6.6 10.8a15 15 0 0 0 6.6 6.6l2.2-2.2a1 1 0 0 1 1-.25 11.4 11.4 0 0 0 3.6.57 1 1 0 0 1 1 1V20a1 1 0 0 1-1 1A17 17 0 0 1 3 4a1 1 0 0 1 1-1h3.5a1 1 0 0 1 1 1c0 1.25.2 2.45.57 3.57a1 1 0 0 1-.25 1z"/></svg>+65 6100 2040</li>
      <li><svg viewBox="0 0 24 24"><path d="M7 1h10a2 2 0 0 1 2 2v18a2 2 0 0 1-2 2H7a2 2 0 0 1-2-2V3a2 2 0 0 1 2-2zm0 3v14h10V4zm5 15.5a1.2 1.2 0 1 0 0 2.4 1.2 1.2 0 0 0 0-2.4z"/></svg>+65 9000 1357</li>
      <li><svg viewBox="0 0 24 24"><path d="M6 2h12v5H6zM4 8h16a2 2 0 0 1 2 2v7h-4v5H6v-5H2v-7a2 2 0 0 1 2-2zm4 8v4h8v-4z"/></svg>+65 6100 2041</li>
      <li><svg viewBox="0 0 24 24"><path d="M2 5h20v14H2zm2 2v.5l8 5.5 8-5.5V7z"/></svg>rohan@arvenco.com</li>
    </ul>
  </div>
</div>
</body>
</html>
```